Automotive Business Card Design

I would just like a automotive themed card. nothing too extravagant, but catchy.

needs to say something about doing roadside assistance,mobile repairs, Diesel repairs, and Fleet maintenance

it can be single sided or double sided. no preference there.

Industry/Entity Type

Automotive

Contact Information for Business Card

Dana Whitcombe
phone 547 391 2084
Name: Brightway Automotive & Diesel Repair

```html
<!DOCTYPE html>
<html lang="en">
<head>
<meta charset="utf-8">
<title>Brightway Automotive &amp; Diesel Repair – Business Card</title>
<link rel="stylesheet" href="https://fonts.googleapis.com/css2?family=Open+Sans:wght@400;700;800&display=swap">
<style>
  :root {
    --page-bg: #e6e3de;
    --card-white: #ffffff;
    --yellow-top: #fad524;
    --yellow-bottom: #f5a81f;
    --orange-top: #f8a43a;
    --orange-bottom: #ec6a1f;
    --ink: #111111;
    --car-dark: #26282b;
    --car-mid: #55585d;
    --engine-dark: #3b3632;
    --engine-mid: #8a7c6e;
    --engine-light: #c9b8a4;
  }
  * { box-sizing: border-box; margin: 0; padding: 0; }
  html, body { width: 1200px; height: 1037px; overflow: hidden; }
  body {
    background: var(--page-bg);
    font-family: "Open Sans", Arial, sans-serif;
    color: var(--ink);
    position: relative;
  }
  .card {
    position: absolute;
    left: 250px;
    width: 700px;
    height: 420px;
    overflow: hidden;
    box-shadow: 0 6px 18px rgba(0,0,0,0.25);
  }
  .card--front { top: 80px; display: flex; }
  .card--back { top: 540px; }

  .front__visual {
    width: 265px;
    height: 100%;
    background: var(--card-white);
    position: relative;
  }
  .front__car {
    position: absolute;
    left: 10px;
    top: 95px;
    width: 255px;
    height: 150px;
    background: radial-gradient(ellipse 50% 42% at 50% 55%,
      var(--car-mid) 0%, var(--car-dark) 55%, rgba(38,40,43,0) 100%);
  }
  .front__details {
    flex: 1;
    background: linear-gradient(180deg, var(--yellow-top), var(--yellow-bottom));
    text-align: center;
    padding: 70px 24px 0;
  }
  .owner-name {
    font-size: 34px;
    font-weight: 800;
    letter-spacing: 3px;
    white-space: nowrap;
  }
  .owner-phone {
    font-size: 20px;
    font-weight: 700;
    letter-spacing: 3px;
    margin-top: 4px;
  }
  .services-title {
    font-size: 20px;
    font-weight: 800;
    margin-top: 48px;
  }
  .services-list {
    list-style: none;
    font-size: 20px;
    line-height: 26px;
    margin-top: 16px;
    letter-spacing: -0.3px;
  }

  .back__photo {
    position: absolute;
    inset: 0;
    background:
      radial-gradient(circle at 65% 60%, var(--engine-light) 0, transparent 35%),
      linear-gradient(135deg, var(--engine-dark), var(--engine-mid) 55%, var(--engine-dark));
  }
  .back__band {
    position: absolute;
    left: 0; right: 0; bottom: 0;
    height: 118px;
    padding: 0 48px;
    background: linear-gradient(180deg, var(--orange-top), var(--orange-bottom));
    display: flex;
    align-items: center;
    justify-content: center;
  }
  .company-name {
    font-size: 26px;
    font-weight: 800;
    text-transform: uppercase;
    letter-spacing: 0.3px;
    white-space: nowrap;
  }
</style>
</head>
<body>
  <section class="card card--front">
    <div class="front__visual">
      <div class="front__car" role="img" aria-label="Photo of a black sports coupe"></div>
    </div>
    <div class="front__details">
      <h1 class="owner-name">Dana Whitcombe</h1>
      <p class="owner-phone">547 391 2084</p>
      <h2 class="services-title">SERVICES</h2>
      <ul class="services-list">
        <li>Roadside assistance</li>
        <li>Mobile repairs</li>
        <li>Diesel repairs</li>
        <li>And Fleet maintenance</li>
      </ul>
    </div>
  </section>

  <section class="card card--back">
    <div class="back__photo" role="img" aria-label="Photo of a hand turning a ratchet wrench on an open engine"></div>
    <div class="back__band">
      <p class="company-name">Brightway Automotive &amp; Diesel Repair</p>
    </div>
  </section>
</body>
</html>
```